The podcast Rivals across a far fence needs cover art

We are launching our podcast soon and need cover art for the podcast platforms (plumvine audio, lumbrel, etc). The aspect ratio is 1:1, so 3000x3000 pixels.
The podcast is about two friends who are on completely opposite sides when it comes to politics and religion (one is a conservative evangelical and the other is a liberal atheist) yet they are good friends. We believe that no matter what your side is, we can be open about our opinions, discuss it and still get along. Our topics include feminism, ghosts, angels, relationships, death and many more.
The design for this art should reflect how we are opposite but still friends, sort of yin and yang. The title is RIVALS ACROSS A FAR FENCE. Perhaps the word "Rivals"and "Far Fence" are larger text than "across a".
I will upload an example (this was created by me quickly, it's pretty bad). And a few art work samples that I like.

Target Market(s)

Adults, ages 18 and up who are interested in discussions about religion, relationships and more

Font styles to use
Sans Serif

Requirements
Must have
• Must be 1:1 aspect ratio. Should give the feeling of opposites but yet together.

```html
<!DOCTYPE html>
<html lang="en">
<head>
<meta charset="utf-8">
<title>Rivals across a far fence — Podcast Cover</title>
<link rel="stylesheet" href="https://fonts.googleapis.com/css2?family=Londrina+Solid:wght@900&family=Great+Vibes&display=swap">
<style>
  :root {
    --page: #ffffff;
    --night: #1f2326;
    --navy: #22315a;
    --steel: #2160a0;
    --salmon: #b2706a;
    --mauve: #a27791;
    --teal: #2a8f8c;
    --deep-teal: #22618a;
    --title: #ffffff;
    --caption: #8a8d94;
  }
  html, body {
    margin: 0;
    width: 1200px;
    height: 1200px;
    overflow: hidden;
    background: var(--page);
  }
  .canvas {
    position: relative;
    width: 1200px;
    height: 1200px;
  }
  .cover-art {
    position: absolute;
    left: 0;
    top: 0;
    width: 1200px;
    height: 1200px;
  }
  .title {
    position: absolute;
    left: 86px;
    width: 1028px;
    margin: 0;
    text-align: center;
    font-family: "Londrina Solid", sans-serif;
    font-weight: 900;
    color: var(--title);
    line-height: 1;
  }
  .title--rivals { top: 114px; font-size: 250px; letter-spacing: 8px; }
  .title--across { top: 369px; font-size: 66px; letter-spacing: 1px; }
  .title--a { top: 594px; font-size: 84px; }
  .title--far { top: 687px; font-size: 215px; letter-spacing: 6px; }
  .title--fence { top: 863px; font-size: 215px; letter-spacing: 6px; }
  .caption {
    position: absolute;
    left: 0;
    width: 1200px;
    top: 1112px;
    margin: 0;
    text-align: center;
    font-family: "Great Vibes", cursive;
    font-size: 44px;
    line-height: 1;
    color: var(--caption);
  }
</style>
</head>
<body>
<main class="canvas">
  <svg class="cover-art" viewBox="0 0 1500 1500" xmlns="http://www.w3.org/2000/svg">
    <defs>
      <linearGradient id="sky" x1="0" y1="0" x2="1" y2="0">
        <stop offset="0" stop-color="var(--night)"/>
        <stop offset="0.4" stop-color="var(--navy)"/>
        <stop offset="1" stop-color="var(--steel)"/>
      </linearGradient>
      <linearGradient id="sea" x1="0" y1="0" x2="0" y2="1">
        <stop offset="0" stop-color="var(--teal)"/>
        <stop offset="1" stop-color="var(--deep-teal)"/>
      </linearGradient>
    </defs>
    <rect class="top-field" x="108" y="88" width="1284" height="400" fill="url(#sky)" role="img" aria-label="Dark brushed texture background"/>
    <rect class="band band--left" x="108" y="483" width="642" height="355" fill="var(--salmon)" role="img" aria-label="Chess pieces illustration, left side"/>
    <rect class="band band--right" x="750" y="483" width="642" height="355" fill="var(--mauve)" role="img" aria-label="Chess pieces illustration, right side, mirrored"/>
    <rect class="bottom-field" x="108" y="835" width="1284" height="535" fill="url(#sea)" role="img" aria-label="Two facing head silhouettes with gears and circles"/>
    <path class="waist waist--top" d="M450 480 C610 480 680 650 750 660 C820 650 890 480 1050 480 Z" fill="var(--navy)"/>
    <path class="waist waist--bottom" d="M450 840 C610 840 680 680 750 668 C820 680 890 840 1050 840 Z" fill="var(--teal)"/>
  </svg>

  <h1 class="title title--rivals">RIVALS</h1>
  <p class="title title--across">ACROSS</p>
  <p class="title title--a">A</p>
  <p class="title title--far">FAR</p>
  <p class="title title--fence">FENCE</p>

  <p class="caption">Podcast Cover art</p>
</main>
</body>
</html>
```